Menu Board 1000mmx500mm re-design

I would like to re-design exiting menu board 1000mmx500mm. Current board letters are bit to small to read. I would like to have pictures (attached) of the food offered on it and at the same time to create balance between pictures and size of the text to be easily readable. Fonts and colours are up to designer choice but prefer warm and bright colours rather anything dark.

Target Market(s)

Food industry

Industry/Entity Type

Food

Font styles to use
Other font styles liked:
• I leave font choice to designer

Colors
FFC000
F8CF3A
FAE287
FDF2CF
FEFAEE
F0912C
F2A743
F7CA91
FBE8D2
FDF5EE
EE7325
F08F49
F5BC92
FAE3D3
FDF4ED

Requirements
Must have
• Pictures + Text
Nice to have
• Balance between images and text.
Should not have
• Can't think of any

```html
<!DOCTYPE html>
<html lang="en">
<head>
<meta charset="utf-8">
<title>Menu Board</title>
<link rel="stylesheet" href="https://fonts.googleapis.com/css2?family=Open+Sans:wght@400;600;800&family=Permanent+Marker&family=Oswald:wght@600&family=Josefin+Sans:wght@700&display=swap">
<style>
  :root {
    --orange: #EE7325;
    --orange-soft: #F08F49;
    --orange-pale: #F5BC92;
    --gold: #F2A743;
    --ink: #2b2b2b;
    --charcoal: #4a4a4a;
    --paper: #ffffff;
    --stage: #efe9e2;
  }
  * { box-sizing: border-box; margin: 0; padding: 0; }
  html, body { width: 1200px; height: 1200px; overflow: hidden; background: var(--stage); }
  .board {
    position: absolute; left: 320px; top: 40px;
    width: 560px; height: 1120px;
    background: var(--paper); overflow: hidden;
    font-family: "Open Sans", Arial, sans-serif;
  }
  .board-art { position: absolute; inset: 0; }
  .menu-banner {
    position: absolute; left: 214px; top: 520px; width: 246px; height: 58px;
    display: flex; align-items: center; justify-content: center;
    font-family: "Permanent Marker", "Arial Black", Arial, sans-serif; font-weight: 700;
    font-size: 46px; line-height: 1; color: var(--paper);
    letter-spacing: 2px; padding-top: 2px; white-space: nowrap;
  }
  .menu-item { position: absolute; left: 64px; width: 456px; }
  .item-head { display: flex; align-items: flex-end; }
  .item-name {
    width: 359px; border-bottom: 1.5px dashed var(--orange-pale);
    color: var(--orange); font-weight: 800; font-size: 23px; line-height: 28px;
    letter-spacing: 0.2px; white-space: nowrap;
  }
  .item-price {
    margin-left: 14px; color: var(--orange); font-weight: 800; font-size: 25px; line-height: 30px;
    white-space: nowrap;
  }
  .item-desc {
    color: var(--ink); font-size: 14.5px; line-height: 17px; font-weight: 400;
    margin-top: 1px; white-space: nowrap;
  }
  .sauces-label {
    position: absolute; left: 30px; top: 1058px;
    font-family: "Oswald", Impact, sans-serif; font-weight: 600; font-size: 52px; line-height: 56px;
    color: var(--paper); letter-spacing: 1px; white-space: nowrap;
  }
  .sauces-list {
    position: absolute; right: 8px; top: 1062px; width: 320px; text-align: right;
    font-family: "Josefin Sans", Arial, sans-serif; font-weight: 700; font-size: 16px; line-height: 22px;
    color: var(--paper); letter-spacing: 1.2px; word-spacing: 5px; white-space: nowrap;
  }
</style>
</head>
<body>
<main class="board">
  <svg class="board-art" width="560" height="1120" viewBox="0 0 560 1120">
    <defs>
      <radialGradient id="potatoes" cx="45%" cy="45%" r="70%">
        <stop offset="0" stop-color="#f4c35a"/>
        <stop offset="0.45" stop-color="#e0a23a"/>
        <stop offset="0.8" stop-color="#b9782a"/>
        <stop offset="1" stop-color="#6f6a62"/>
      </radialGradient>
      <radialGradient id="dish" cx="50%" cy="45%" r="60%">
        <stop offset="0" stop-color="#f1e6cf"/>
        <stop offset="1" stop-color="#a7723f"/>
      </radialGradient>
    </defs>
    <rect class="hero-photo" role="img" aria-label="Photo of golden roasted potatoes with thyme" x="0" y="0" width="560" height="460" fill="url(#potatoes)"/>
    <path d="M470 0 C455 110 440 250 360 320 C290 380 200 400 120 440 L0 470 L0 560 L560 560 L560 0 Z" fill="var(--paper)"/>
    <path d="M470 0 C455 110 440 250 360 320" fill="none" stroke="var(--orange)" stroke-width="8"/>

    <g stroke="var(--orange)" stroke-width="9">
      <circle role="img" aria-label="Photo of toasted wrap halves" cx="484" cy="101" r="50" fill="url(#dish)"/>
      <circle role="img" aria-label="Photo of beetroot wrap halves" cx="484" cy="228" r="50" fill="#b9667a"/>
      <circle role="img" aria-label="Photo of chicken ciabatta sandwich" cx="429" cy="356" r="62" fill="url(#dish)"/>
      <circle role="img" aria-label="Photo of grilled chicken wrap" cx="274" cy="431" r="66" fill="url(#dish)"/>
      <circle role="img" aria-label="Photo of roast chicken quarter with vegetable rice" cx="102" cy="450" r="82" fill="#a1632f"/>
    </g>

    <path d="M214 520 H460 L452 549 L460 578 H232 L226 592 L214 578 Z" fill="var(--orange)"/>
    <path d="M214 578 L226 592 L232 578 Z" fill="#b9531a"/>

    <rect x="0" y="1052" width="560" height="68" fill="var(--charcoal)"/>
    <path d="M0 1052 H230 C250 1052 262 1060 256 1072 L240 1120 H0 Z" fill="var(--orange)"/>
  </svg>

  <div class="menu-banner">MENU</div>

  <section class="menu-list">
    <article class="menu-item" style="top:590px">
      <div class="item-head"><h2 class="item-name">CIABATTA</h2><span class="item-price">£6</span></div>
      <p class="item-desc">Roti Chicken, Rucola, Caramelized Onions,<br>Tomato, Fresh Onion</p>
    </article>
    <article class="menu-item" style="top:658px">
      <div class="item-head"><h2 class="item-name">WRAP</h2><span class="item-price">£7</span></div>
      <p class="item-desc">Roti Chicken, Crunchy Slaw, Tomato,<br>Fresh Onion &amp; Sauce of your choice</p>
    </article>
    <article class="menu-item" style="top:728px">
      <div class="item-head"><h2 class="item-name">BEETROOT WRAP</h2><span class="item-price">£8</span></div>
      <p class="item-desc">Roti Chicken, Crunchy Slaw, Tomato,<br>Fresh Onion &amp; Sauce of your choice</p>
    </article>
    <article class="menu-item" style="top:799px">
      <div class="item-head"><h2 class="item-name">1/4 CHICKEN BOX</h2><span class="item-price">£9</span></div>
      <p class="item-desc">Roti Chicken, Veggie Rice &amp; Salad</p>
    </article>
    <article class="menu-item" style="top:852px">
      <div class="item-head"><h2 class="item-name">1/2 CHICKEN BOX</h2><span class="item-price">£14</span></div>
      <p class="item-desc">Roti Chicken, Veggie Rice &amp; Salad</p>
    </article>
    <article class="menu-item" style="top:906px">
      <div class="item-head"><h2 class="item-name">ROASTED POTATOES</h2><span class="item-price">£2.5</span></div>
      <p class="item-desc">Thyme &amp; Garlic</p>
    </article>
    <article class="menu-item" style="top:960px">
      <div class="item-head"><h2 class="item-name">WATER</h2><span class="item-price">£1</span></div>
    </article>
    <article class="menu-item" style="top:996px">
      <div class="item-head"><h2 class="item-name">CAN &amp; JUICES</h2><span class="item-price">£1.8</span></div>
    </article>
  </section>

  <h2 class="sauces-label">SAUCES</h2>
  <p class="sauces-list">SIGNATURE BBQ PIRI PIRI<br>SWEET CHILLI GARLIC MAYO</p>
</main>
</body>
</html>
```